Kneadwell Points website re-design and

the academy of bodywork studies is ready for a new website. The current website is around 12 years old and it looks old. Luckily the clients is not against changing the colors so the new design does not have to use the current ugly green color scheme. Be creative! Make it pretty, modern and inviting. The current colors look like mold. Nobody likes mold. I have attached the logo asset file as well as a txt document that details the new website design parameters

1 page

```html
<!DOCTYPE html>
<html lang="en">
<head>
<meta charset="utf-8">
<title>Kneadwell Points – Academy of Bodywork Studies</title>
<link rel="stylesheet" href="https://fonts.googleapis.com/css2?family=Jost:wght@400;500;600&display=swap">
<style>
:root{
  --red:#d9533f;
  --beige:#f5dcc0;
  --yellow:#ece88a;
  --gold:#d9b96a;
  --grey:#ececec;
  --ink:#222;
  --soft:#666;
  --white:#fff;
  --list:#7a3b3b;
}
*{box-sizing:border-box;margin:0;padding:0}
html,body{width:1200px;height:4777px;overflow:hidden}
body{position:relative;font-family:"Jost",sans-serif;color:var(--ink);background:var(--white)}
.abs{position:absolute}
.photo{position:absolute}
.brand{position:absolute;display:flex;align-items:center;gap:8px;font-size:15px;font-weight:500;color:var(--ink);letter-spacing:.5px}
.brand .mark{width:12px;height:12px;background:var(--ink)}
/* header */
.nav{position:absolute;left:343px;top:25px;display:flex;gap:26px;font-size:12px}
.btn-login{position:absolute;left:862px;top:21px;width:71px;height:26px;background:#e9846f;color:#fff;font-size:11px;display:flex;align-items:center;justify-content:center;border-radius:3px}
.cart{position:absolute;left:970px;top:24px;font-size:11px;display:flex;align-items:center;gap:6px}
/* hero */
.hero-title{position:absolute;left:577px;top:163px;width:389px;height:232px;background:#fff;padding:68px 20px 0 32px;font-size:26px;line-height:33px}
.search{position:absolute;left:857px;top:445px;width:343px;height:208px;background:var(--red);color:#fff;padding:32px 44px}
.search h3{font-weight:400;font-size:15px;line-height:17px}
.search .field{border-bottom:1px solid rgba(255,255,255,.7);font-size:10px;padding:12px 3px 6px;width:214px}
.search .go{margin-top:22px;width:78px;height:28px;border:1.5px solid #fff;border-radius:5px;font-size:11px;display:flex;align-items:center;justify-content:center}
/* about */
.about h2{position:absolute;left:237px;top:674px;font-weight:400;font-size:29px;line-height:34px}
.about p{position:absolute;left:237px;top:770px;width:366px;font-size:12.6px;line-height:22.3px;color:var(--soft)}
.ring{position:absolute;left:692px;top:732px;width:390px;height:390px;border-radius:50%;background:var(--yellow)}
/* popular */
.popular{position:absolute;left:0;top:1178px;width:1200px;height:531px;background:var(--beige)}
.section-title{position:absolute;font-weight:400;font-size:28px;text-align:center}
.card{position:absolute;background:#fff}
.card h4{font-size:13px;font-weight:500}
.card p{font-size:10px;line-height:16px;color:var(--soft);margin-top:10px}
/* best */
.best-item{position:absolute;top:1829px;width:169px}
.best-item .pic{height:141px}
.best-item h5{font-weight:400;font-size:13.5px;line-height:19px;margin-top:12px;padding-left:6px}
.best-item small{display:block;color:var(--red);font-size:9.5px;margin-top:4px;padding-left:6px}
/* free */
.free{position:absolute;left:0;top:2105px;width:1200px;height:340px;background:var(--red)}
.free h2{position:absolute;left:519px;top:84px;color:#fff;font-size:46px;font-weight:400}
.free p{position:absolute;left:529px;top:146px;color:#fff;font-size:20px;line-height:28px;width:345px}
.free .rule{position:absolute;left:529px;top:219px;width:110px;height:2px;background:#fff}
.vertical{position:absolute;left:150px;top:2135px;width:30px;height:230px;writing-mode:vertical-rl;transform:rotate(180deg);font-size:13px;letter-spacing:1.5px;color:var(--ink);text-align:center}
/* reasons */
.reasons-title{position:absolute;left:267px;top:2600px;font-size:25px;line-height:32px;font-weight:400}
.pill{position:absolute;left:234px;height:34px;border:1.5px solid var(--ink);font-size:11.5px;display:flex;align-items:center;padding:0 12px;background:#fff}
.pill.active{background:var(--red);color:#fff;border-color:var(--red);height:29px}
.risk{position:absolute;left:529px;top:2807px;width:437px;height:332px;background:#fff;padding:48px 28px 0 36px}
.risk h4{font-weight:400;font-size:17px}
.risk p{font-size:11.6px;line-height:19.5px;color:var(--soft);margin-top:16px}
/* faq */
.faq{position:absolute;left:234px;top:3265px;width:499px}
.faq .item{border-bottom:1.5px solid #555;display:flex;justify-content:space-between;align-items:flex-start;padding:10px 8px 0 8px;font-size:12px;line-height:18px}
.faq .item span.q{width:440px}
.faq .item b{font-weight:400;font-size:20px;line-height:18px}
.faq .answer{font-size:11.6px;line-height:18px;color:var(--soft);margin-top:30px}
.faq-box{position:absolute;left:777px;top:3306px;width:423px;height:159px;background:var(--gold);border-radius:24px 0 0 24px;color:#fff;font-size:17px;line-height:21px;padding:78px 30px 0 27px}
.faq-box span{display:block;width:255px}
.contact-note{position:absolute;left:812px;top:3701px;width:162px;height:241px;background:#e9846f;color:#fff;font-style:italic;font-size:11.6px;line-height:16px;padding:34px 22px 0 22px;font-weight:500}
.contact-note .rule{width:58px;height:2px;background:#fff;margin-top:6px}
/* titles */
.titles-box{position:absolute;left:52px;top:4257px;width:1109px;height:329px;background:#f2f2f2}
.titles-head{position:absolute;left:390px;top:4235px;width:367px;height:47px;background:#fff;border:1.5px solid #555;border-radius:5px;font-size:26px;display:flex;align-items:center;justify-content:center}
.col{position:absolute;top:4328px;font-size:8.6px;line-height:18.2px;color:var(--list);list-style:none;white-space:nowrap}
/* footer */
.footer{position:absolute;left:0;top:4586px;width:1200px;height:185px;background:#eadc84}
.footer .login{position:absolute;left:241px;top:94px;width:149px;height:32px;border:1.5px solid var(--ink);border-radius:4px;background:#fff;font-size:11px;display:flex;align-items:center;justify-content:center}
.footer ul{position:absolute;left:464px;top:38px;list-style:none;font-size:9.6px;line-height:15.4px}
.footer .copy{position:absolute;left:744px;top:80px;font-size:9.6px;line-height:15px}
.bottom-line{position:absolute;left:0;top:4771px;width:1200px;height:6px;background:var(--red)}
</style>
</head>
<body>

<!-- header -->
<div class="brand" style="left:93px;top:22px"><span class="mark"></span>Academy of Bodywork Studies</div>
<nav class="nav"><span>Home</span><span>About Us</span><span>Courses</span><span>Guidelines</span><span>Faqs</span><span>Policies</span><span>Contact Us</span></nav>
<div class="btn-login">Login</div>
<div class="cart">
  <svg width="16" height="16" viewBox="0 0 16 16" fill="none" stroke="#222" stroke-width="1.3"><path d="M3 5h10l-1 9H4z"/><path d="M6 5V3.5a2 2 0 0 1 4 0V5"/></svg>
  Cart: 0 item(s)
</div>

<!-- hero -->
<div class="photo" style="left:0;top:67px;width:33px;height:495px;background:var(--yellow)"></div>
<div class="abs" style="left:12px;top:468px;width:8px;height:8px;border-radius:50%;background:#e9846f"></div>
<div class="abs" style="left:12px;top:488px;width:8px;height:8px;border-radius:50%;background:#fff"></div>
<div class="photo" role="img" aria-label="Therapist massaging a relaxed client's back" style="left:33px;top:67px;width:824px;height:495px;background:linear-gradient(120deg,#8a6a58,#d8b9a4 45%,#ecdcd0)"></div>
<div class="photo" role="img" aria-label="Client receiving a facial massage" style="left:857px;top:67px;width:343px;height:378px;background:linear-gradient(160deg,#e9d8cc,#c9a28c)"></div>
<div class="hero-title">Committed to Excellence in Massage Therapy Continuing Education</div>
<form class="search">
  <h3>Search<br>online courses</h3>
  <div class="field">Search by keyword</div>
  <div class="field" style="margin-top:10px">Number of CE Hours</div>
  <div class="go">Search</div>
</form>

<!-- about -->
<section class="about">
  <div class="photo" role="img" aria-label="Leaf decoration" style="left:1060px;top:660px;width:130px;height:110px;background:#fbe9d8;border-radius:50%"></div>
  <div class="photo" role="img" aria-label="Leaf decoration" style="left:0;top:1010px;width:150px;height:120px;background:#f3ef9f;border-radius:50%"></div>
  <h2>The Academy<br>of Bodywork Studies</h2>
  <p>The Academy of Bodywork Studies is committed to providing the best online home study continuing education courses available to massage therapists. Academy of Bodywork Studies is approved by the National Bodywork Credential Council (NBCC) as a continuing education Approved Provider. Provider # 415208-00. Our massage CEUs/credits are also valid for AMPA and BWG. We are approved by the Florida Board of Massage (Provider #MCE804) and CredTrack (Provider #50-7720). Our massage therapy continuing education courses are valid for most state massage therapy CEU requirements. See our State Guidelines page for specific information about the continuing education laws in your state.</p>
  <div class="ring"></div>
  <div class="photo" role="img" aria-label="Client relaxing during a massage" style="left:674px;top:742px;width:352px;height:352px;border-radius:50%;background:linear-gradient(140deg,#d9c0ad,#8f6d5b)"></div>
  <div class="photo" role="img" aria-label="Leaf decoration" style="left:1030px;top:1090px;width:80px;height:110px;background:#f0c98a;border-radius:50%"></div>
</section>

<!-- popular -->
<section class="popular">
  <div class="photo" role="img" aria-label="Smiling woman relaxing on a massage table" style="left:0;top:0;width:340px;height:531px;background:linear-gradient(90deg,#c7a38b,#e8d3c2 80%,var(--beige))"></div>
  <div class="abs" style="left:170px;top:30px;width:42px;height:2px;background:#222"></div>
  <h2 class="section-title" style="left:430px;top:52px;width:340px">Our Popular Courses</h2>
  <div class="card" style="left:288px;top:128px;width:222px;height:328px;padding:22px 20px">
    <div role="img" aria-label="Pregnant women in an exercise class" style="height:114px;border-radius:8px;background:linear-gradient(135deg,#b9d3dc,#7fa8b6)"></div>
    <h4 style="margin-top:66px">Pregnancy / Doula</h4>
    <p>Courses and packages to become certified in every stage of childbearing, from infertility to infant massage</p>
  </div>
  <div class="card" style="left:529px;top:128px;width:437px;height:150px;padding:16px 12px;display:flex;gap:16px">
    <div role="img" aria-label="Gavel and law book" style="width:188px;height:118px;flex:none;border-radius:8px;background:linear-gradient(135deg,#5a2b1c,#b46a36)"></div>
    <div><h4 style="margin-top:0">Florida Laws &amp; Packages</h4><p style="margin-top:22px">Courses and packages required to obtain, reinstate, or renew your Florida massage therapy license</p></div>
  </div>
  <div class="card" style="left:529px;top:308px;width:437px;height:148px;padding:16px 12px;display:flex;gap:16px">
    <div role="img" aria-label="Person writing research notes" style="width:188px;height:118px;flex:none;border-radius:8px;background:linear-gradient(135deg,#dfe6ee,#4a5d80)"></div>
    <div><h4 style="margin-top:20px">Research Courses</h4><p style="margin-top:6px">Courses approved by the NBCC to earn mandated research hours for Board Certification renewal</p></div>
  </div>
</section>

<!-- best selling -->
<h3 class="section-title" style="left:234px;top:1760px;width:732px;font-size:16.5px">Best selling courses</h3>
<div class="abs" style="left:234px;top:1796px;width:732px;height:1.5px;background:#333"></div>
<div class="best-item" style="left:234px"><div class="pic" role="img" aria-label="Abdominal massage" style="background:linear-gradient(135deg,#e9ded5,#b58f79)"></div><h5>Certified Fertility<br>Massage Therapist</h5><small>Credit Hours: 16</small></div>
<div class="best-item" style="left:423px"><div class="pic" role="img" aria-label="Infant foot massage" style="background:linear-gradient(135deg,#f1d2c2,#c88f76)"></div><h5>Certified Infant Massage<br>Therapist–Instructor</h5><small>Credit Hours: 16</small></div>
<div class="best-item" style="left:608px"><div class="pic" role="img" aria-label="Pregnant client massage" style="background:linear-gradient(135deg,#c08a6d,#6f4a38)"></div><h5>Certified Massage Doula</h5><small>Credit Hours: 21</small></div>
<div class="best-item" style="left:798px"><div class="pic" role="img" aria-label="Leg and hip massage" style="background:linear-gradient(135deg,#e6ddd6,#9d8577)"></div><h5>Anatomy Fascial Lines</h5><small>Credit Hours: 25</small></div>

<!-- free course -->
<section class="free">
  <div class="abs" style="left:135px;top:0;width:54px;height:285px;background:#fff"></div>
  <div class="photo" role="img" aria-label="Woman relaxing during a back massage" style="left:189px;top:0;width:266px;height:287px;background:linear-gradient(150deg,#d8bfae,#8b6650)"></div>
  <div class="photo" role="img" aria-label="Leaf decoration" style="left:1000px;top:95px;width:85px;height:130px;background:#efa646;border-radius:50%"></div>
  <h2>Take a free course</h2>
  <p>Click here to get started today and try our FREE online course!</p>
  <div class="rule"></div>
</section>
<div class="vertical">Academy of Bodywork Studies</div>
<div class="photo" role="img" aria-label="Tropical leaf" style="left:66px;top:2280px;width:85px;height:80px;background:#3f7a3a;border-radius:50%"></div>
<div class="abs" style="left:52px;top:2366px;width:292px;height:181px;background:#fff"></div>
<div class="photo" role="img" aria-label="Woman with long hair beside a tropical leaf" style="left:61px;top:2380px;width:269px;height:156px;background:linear-gradient(135deg,#c99072,#7a4a33)"></div>
<div class="photo" role="img" aria-label="Tropical leaf" style="left:330px;top:2390px;width:160px;height:150px;background:#3e7b38;border-radius:50%"></div>

<!-- reasons -->
<h2 class="reasons-title">Three reasons why the<br>Academy of Bodywork Studies offers<br>best online continuing education experience</h2>
<div class="abs" style="left:0;top:2736px;width:800px;height:455px;background:var(--grey)"></div>
<div class="photo" role="img" aria-label="Client receiving a face massage" style="left:811px;top:2584px;width:389px;height:634px;background:linear-gradient(160deg,#e7d2c4,#a97a62 60%,#6d4a3b)"></div>
<div class="photo" role="img" aria-label="Essential oil bottles, lemon and leafy sprigs" style="left:0;top:2736px;width:210px;height:455px;background:linear-gradient(180deg,#e5ece0,#f3efd5 60%,#f3d57a)"></div>
<div class="pill" style="top:2877px;width:181px">Instant Access and Results</div>
<div class="pill active" style="top:2922px;width:104px">Hassle-Free</div>
<div class="pill" style="top:2964px;width:170px">Risk free sample course</div>
<div class="pill" style="top:3014px;width:265px">And if those three reasons aren't enough</div>
<article class="risk">
  <h4>Risk free sample course</h4>
  <p>Take a free course to see exactly how our system operates. This gives you the peace of mind of knowing what to expect before you commit to any of our courses. Feel free to see how well you do with an online learning and testing format. You can test the course from two perspectives: while you are taking it, and when you are finished with it. You will see how you can log in and out during the course and/or navigate through it, and how you have access to course materials, test results, and certificates once you have completed the course.</p>
</article>
<div class="photo" role="img" aria-label="Leaf decoration" style="left:0;top:3150px;width:140px;height:110px;background:#f3ef9f;border-radius:50%"></div>

<!-- faq -->
<div class="faq">
  <div class="item" style="height:62px"><span class="q">I am currently in massage school. Can I start taking your pregnancy massage course now so when I become licensed I'll be ready to work on pregnant women?</span><b>+</b></div>
  <div class="item" style="height:46px;padding-top:20px"><span class="q">Do I have to be a licensed massage therapist to take your courses?</span><b>+</b></div>
  <div class="item" style="height:45px;padding-top:18px"><span class="q">Are your online courses downloadable to my computer?</span><b>+</b></div>
  <div class="item" style="height:45px;padding-top:18px"><span class="q">Will your online courses work on my phone, tablet, or other device?</span><b>+</b></div>
  <div class="item" style="height:59px;padding-top:16px"><span class="q">Can I log in and out while taking an online course, or do I have to take it all at once?</span><b>+</b></div>
  <div class="item" style="height:50px;padding-top:24px"><span class="q">How do I print an additional certificate?</span><b>+</b></div>
  <div class="item" style="height:202px;padding-top:22px;display:block">
    <div style="display:flex;justify-content:space-between"><span class="q">Does the Academy of Bodywork Studies automatically report course completions to CredTrack?</span><b>–</b></div>
    <p class="answer">Yes, we automatically report all course completions to CredTrack provided that your Florida Massage license number was listed on your account before you completed our online test. You can verify or edit your license information when you log into our account and review the General Information that appears to the left of the page.</p>
  </div>
  <div class="item" style="height:70px;padding-top:24px;border-bottom:none"><span class="q">Does the Academy of Bodywork Studies report our course completions to the NBCC, AMPA, BWG, or any other agencies or state massage therapy boards?</span><b>+</b></div>
</div>
<div class="faq-box"><span>Frequently asked questions about our online continuing education courses</span></div>
<div class="photo" role="img" aria-label="Leaf decoration" style="left:1080px;top:3270px;width:100px;height:110px;background:#f0c98a;border-radius:50%"></div>
<div class="photo" role="img" aria-label="Hot stone massage with candles" style="left:777px;top:3506px;width:197px;height:182px;background:linear-gradient(135deg,#3a2a22,#c98c5c)"></div>
<div class="photo" role="img" aria-label="Therapist working on a client" style="left:981px;top:3550px;width:201px;height:138px;background:linear-gradient(135deg,#e3e6ea,#7d8796)"></div>
<div class="contact-note">Please feel free to contact us at the above contact link if you have any questions about how we can help you attain your continuing education goals. Thank you.<div class="rule"></div></div>
<div class="photo" role="img" aria-label="Spa towels, stones and aroma diffuser" style="left:981px;top:3697px;width:197px;height:180px;background:linear-gradient(135deg,#e9ece4,#8aa07a)"></div>

<!-- course titles -->
<div class="photo" role="img" aria-label="Massage class with students at tables" style="left:0;top:3988px;width:1200px;height:278px;background:linear-gradient(90deg,#6a5548,#c9a48c 35%,#b2856a 65%,#5e4a3f)"></div>
<div class="titles-box"></div>
<div class="titles-head">Available course titles</div>
<ul class="col" style="left:76px">
  <li>Certified Fertility Massage Therapist</li><li>Certified Massage Doula</li><li>Customize Your Own Package</li><li>Anatomy Fascial Lines</li><li>Board Certified Renewal, Package 1</li><li>Board Certified Renewal, Package 3</li><li>Deep Tissue Therapy</li><li>Draping Your Client (Ethics Standard V)</li><li>Ethics - Communication</li><li>Ethics - Listening</li><li>Facilitated PNF Stretching</li><li>Florida Laws &amp; Rules - 10 hours #20-551072</li><li>Florida Renewal 6 CE package - Laws, PME, Ethics</li>
</ul>
<ul class="col" style="left:325px">
  <li>Human Trafficking Awareness and Prevention, 1 CE</li><li>Maryland Package</li><li>Orthopedic Massage for the Extremities</li><li>Pathology - Deep Vein Thrombosis</li><li>Pathology - Morton Foot Structure</li><li>Pathology - Sciatic Pain</li><li>Pathology - Varicose Veins</li><li>Prenatal Massage Techniques (Step Two)</li><li>Reflexology for Feet and Hands</li><li>Research - Pregnancy and Labor Massage</li><li>Seven Mistakes Massage Therapists Make (And How To Avoid Them)</li><li>Sports &amp; Exercise Massage</li>
</ul>
<ul class="col" style="left:662px">
  <li>Certified Infant Massage Therapist–Instructor</li><li>Certified Prenatal Massage Therapist</li><li>100 CE Package</li><li>Aromatherapy for Massage</li><li>Board Certified Renewal, Package 2</li><li>Communicable Diseases &amp; HIV</li><li>Diversity and Cultural Awareness</li><li>Ethics - Boundary Setting (Standard V)</li><li>Ethics - Confidentiality</li><li>Ethics - Professionalism</li><li>Fibromyalgia (Stop the Suffering)</li><li>Florida Laws &amp; Rules - 2 hours #20-48833</li><li>Hot Stone Massage</li>
</ul>
<ul class="col" style="left:903px">
  <li>Human Trafficking Awareness and Prevention, 2 CEs</li><li>New York Package</li><li>Orthopedic Massage for the Spine</li><li>Pathology - Edema</li><li>Pathology - Plantar Fasciitis</li><li>Pathology - Shoulder Dysfunction</li><li>Prenatal Massage Fundamentals (Step One)</li><li>Prevention of Medical Errors for Massage</li><li>Research - Infant Massage</li><li>Research - Reflexology</li><li>Spa Therapy Techniques</li><li>Stretching Anatomy</li>
</ul>

<!-- footer -->
<footer class="footer">
  <div class="photo" role="img" aria-label="Leaf decoration" style="left:60px;top:40px;width:140px;height:130px;background:#f3ef9f;border-radius:50%"></div>
  <div class="brand" style="left:241px;top:56px;font-size:13px"><span class="mark"></span>Academy of Bodywork Studies</div>
  <div class="login">Login to Your Courses</div>
  <ul>
    <li>Home</li><li>Contact Academy of Bodywork Studies</li><li>Courses Offered by Academy of Bodywork Studies</li><li>About Bodywork Studies Academy</li><li>Our Policies</li><li>Guidelines</li><li>Online Courses FAQs</li>
  </ul>
  <div class="copy">© Copyright 2022 Academy of Bodywork Studies.<br>All rights reserved.</div>
</footer>
<div class="bottom-line"></div>

</body>
</html>
```